Technical Redesign of AI-Generated Method & Topic Graphics for PowerPoint

e have a set of graphics and diagrams that were initially created using AI. The content, structure, and overall layout are already defined and should remain largely unchanged.

The objective is NOT to create completely new designs. This is primarily a technical refinement and conversion project. The graphics need to be professionally redrawn, cleaned up, and rebuilt so that they:

• Look less AI-generated and more professional/corporate
• Match our existing corporate website style
• Are fully editable in Microsoft PowerPoint
• Use consistent fonts, colors, spacing, and iconography
• Maintain the original meaning and information structure

REFERENCE WEBSITE
https://moorwald-forschung. at/

Please use the website as the primary reference for:
• Color palette
• Typography
• Visual language
• General corporate look and feel
• Professional, research-oriented appearance

The style should be clean, technical, modern, and suitable for a scientific/research institution.

SCOPE OF WORK
For each supplied graphic:

1. Recreate the graphic manually
- Do not simply trace or export the AI image.
- Rebuild all elements using PowerPoint native objects where possible.

2. Improve visual quality
- Remove typical AI-generated inconsistencies.
- Correct alignment, spacing, proportions, and visual hierarchy.
- Standardize icons and graphic elements.

3. Corporate style adaptation
- Apply colors and typography consistent with our website.
- Use a professional and technically oriented visual style.
- Avoid decorative or overly creative design elements.

4. Ensure full editability
- All text must remain editable.
- Shapes should be editable PowerPoint objects.
- Icons should preferably be vector-based.
- Elements should not be flattened into images unless absolutely necessary.

DELIVERABLES
Required output:

• Microsoft PowerPoint (.pptx)
• All graphics fully editable
• Layered and logically grouped objects
• Consistent formatting across all graphics
• Optional source files (.svg, .ai, or . eps) if available

DESIGN DIRECTION
Please focus on:

• Technical accuracy
• Professional presentation quality
• Corporate consistency
• PowerPoint usability

Please do NOT focus on:
• Creating alternative concepts
• Artistic reinterpretations
• Major layout changes
• Creative redesigns

The goal is to transform existing AI-generated diagrams into professional, corporate-standard, PowerPoint-editable graphics that fit seamlessly with the Moorwaldinstitut Graz website and presentation materials.

```html
<!DOCTYPE html>
<html lang="en">
<head>
<meta charset="utf-8">
<title>Integrated Process Assessment for Technology and Product Innovation</title>
<link rel="stylesheet" href="https://fonts.googleapis.com/css2?family=Source+Sans+3:ital,wght@0,400;0,600;0,700;1,600&display=swap">
<style>
:root{
  --navy:#12288a;
  --navy-soft:#e8ecf4;
  --panel:#eaeef6;
  --green:#3f7a12;
  --teal:#16818a;
  --orange:#ee7812;
  --ink:#1d1d1f;
  --white:#ffffff;
}
*{box-sizing:border-box;margin:0;padding:0}
html,body{width:1200px;height:926px;overflow:hidden;background:var(--white)}
body{font-family:"Source Sans 3",Arial,sans-serif;color:var(--ink);position:relative}
.frame{position:absolute;left:42px;top:32px;width:1115px;height:861px;border:1.5px solid #222}
.abs{position:absolute}
.title{left:0;width:1200px;top:82px;text-align:center;font-size:29px;font-weight:700;color:var(--navy);letter-spacing:-.2px}
.subtitle{left:0;width:1200px;top:117px;text-align:center;font-size:19px;font-weight:600;color:var(--navy)}
.box{position:absolute;border:2px solid var(--navy);border-radius:7px;background:var(--white)}
.start{left:83px;top:168px;width:293px;height:166px}
.start-head{position:absolute;left:74px;top:11px;font-size:16px;font-weight:700;color:var(--navy);line-height:20px}
.start-list{position:absolute;left:18px;top:62px;list-style:none;font-size:11.4px;line-height:21.3px}
.start-list li::before{content:"•";color:var(--navy);margin-right:12px}
.process{left:412px;top:168px;width:636px;height:166px}
.process-head{position:absolute;left:0;width:100%;top:10px;text-align:center;font-size:16px;font-weight:600;color:var(--navy)}
.stage-icon{position:absolute;top:206px;width:58px;height:58px;border-radius:50%;background:var(--navy-soft)}
.stage-icon svg{width:58px;height:58px}
.stage-label{position:absolute;top:284px;width:120px;margin-left:-60px;text-align:center;font-size:14px;font-weight:600;color:var(--navy)}
.pillar{position:absolute;top:349px;height:234px;border:2px solid;border-radius:7px;background:var(--white)}
.pillar h2{position:absolute;left:0;width:100%;top:10px;text-align:center;font-size:18.5px;line-height:23px;font-weight:700}
.pillar ul{position:absolute;list-style:none;font-size:11.6px;line-height:14.6px}
.pillar li{position:relative;margin-bottom:8.5px}
.pillar li::before{content:"";position:absolute;left:-14px;top:4px;width:5px;height:5px;border-radius:50%}
.elca{left:83px;width:319px;border-color:var(--green)}
.elca h2{color:var(--green)} .elca li::before{background:var(--green)}
.elca ul{left:106px;top:74px;width:205px}
.slca{left:422px;width:302px;border-color:var(--teal)}
.slca h2{color:var(--teal)} .slca li::before{background:var(--teal)}
.slca ul{left:97px;top:74px;width:200px}
.lcc{left:743px;width:307px;border-color:var(--orange)}
.lcc h2{color:var(--orange)} .lcc li::before{background:var(--orange)}
.lcc ul{left:115px;top:74px;width:190px}
.pillar-art{position:absolute;border-radius:50%}
.balance{left:413px;top:605px;width:307px;height:62px}
.balance-text{position:absolute;left:92px;top:7px;font-size:19px;font-weight:600;line-height:23px;color:var(--navy)}
.benefits{left:214px;top:690px;width:716px;height:141px;background:var(--panel)}
.benefits h2{position:absolute;left:172px;top:12px;font-size:22px;font-weight:700;color:var(--navy)}
.benefit{position:absolute;font-size:12.6px;line-height:14.4px;padding-left:22px}
.benefit svg{position:absolute;left:0;top:0;width:15px;height:15px}
.footer-text{left:374px;top:854px;font-size:15px;font-style:italic;font-weight:600;color:var(--navy)}
.overlay{position:absolute;left:0;top:0;pointer-events:none}
</style>
</head>
<body>
<div class="frame"></div>

<h1 class="abs title">Integrated Process Assessment for Technology and Product Innovation</h1>
<p class="abs subtitle">Ecological, social and economic assessment in early development phases</p>

<!-- Starting point -->
<section class="box start">
  <svg class="abs" style="left:12px;top:6px" width="54" height="54" viewBox="0 0 54 54" aria-hidden="true">
    <circle cx="25" cy="29" r="22" fill="none" stroke="var(--navy)" stroke-width="5"/>
    <circle cx="25" cy="29" r="13" fill="none" stroke="var(--navy)" stroke-width="5"/>
    <circle cx="25" cy="29" r="4.5" fill="var(--navy)"/>
    <line x1="25" y1="29" x2="46" y2="8" stroke="var(--navy)" stroke-width="3"/>
    <path d="M42 4 L50 4 L50 12 L44 10 Z" fill="var(--navy)"/>
  </svg>
  <div class="start-head">Starting Point &amp;<br>Methodological Foundations</div>
  <ul class="start-list">
    <li>Products, processes, services and systems</li>
    <li>Market, societal and sustainability requirements</li>
    <li>Goal and scope definition</li>
    <li>Reference system, data basis</li>
    <li>Scenarios and sensitivities</li>
  </ul>
</section>

<!-- Innovation process -->
<section class="box process">
  <div class="process-head">Assessment along the innovation process</div>
</section>

<div class="stage-icon" style="left:432px"><svg viewBox="0 0 58 58" aria-hidden="true"><circle cx="25" cy="25" r="11" fill="none" stroke="var(--navy)" stroke-width="2.5"/><line x1="33" y1="33" x2="42" y2="42" stroke="var(--navy)" stroke-width="4" stroke-linecap="round"/></svg></div>
<div class="stage-icon" style="left:540px"><svg viewBox="0 0 58 58" aria-hidden="true"><path d="M29 15a10 10 0 0 0-6 18v5h12v-5a10 10 0 0 0-6-18z" fill="none" stroke="var(--navy)" stroke-width="2"/><line x1="24" y1="41" x2="34" y2="41" stroke="var(--navy)" stroke-width="2"/><line x1="25" y1="44" x2="33" y2="44" stroke="var(--navy)" stroke-width="2"/><g stroke="var(--navy)" stroke-width="1.6"><line x1="29" y1="8" x2="29" y2="11"/><line x1="16" y1="14" x2="18" y2="16"/><line x1="42" y1="14" x2="40" y2="16"/><line x1="12" y1="25" x2="15" y2="25"/><line x1="46" y1="25" x2="43" y2="25"/></g></svg></div>
<div class="stage-icon" style="left:642px"><svg viewBox="0 0 58 58" aria-hidden="true"><circle cx="29" cy="29" r="6" fill="none" stroke="var(--navy)" stroke-width="2"/><circle cx="29" cy="29" r="12" fill="none" stroke="var(--navy)" stroke-width="2"/><g stroke="var(--navy)" stroke-width="4"><line x1="29" y1="13" x2="29" y2="17"/><line x1="29" y1="41" x2="29" y2="45"/><line x1="13" y1="29" x2="17" y2="29"/><line x1="41" y1="29" x2="45" y2="29"/><line x1="18" y1="18" x2="21" y2="21"/><line x1="37" y1="37" x2="40" y2="40"/><line x1="40" y1="18" x2="37" y2="21"/><line x1="18" y1="40" x2="21" y2="37"/></g></svg></div>
<div class="stage-icon" style="left:746px"><svg viewBox="0 0 58 58" aria-hidden="true"><g fill="none" stroke="var(--navy)" stroke-width="2.4" stroke-linejoin="round"><path d="M29 12 L45 20 L45 38 L29 46 L13 38 L13 20 Z"/><path d="M13 20 L29 28 L45 20 M29 28 L29 46"/></g></svg></div>
<div class="stage-icon" style="left:855px"><svg viewBox="0 0 58 58" aria-hidden="true"><g fill="var(--navy)"><rect x="36" y="12" width="5" height="12"/><path d="M12 44 V24 L22 30 V24 L32 30 V24 L46 24 V44 Z"/></g><g fill="var(--navy-soft)"><rect x="16" y="36" width="5" height="5"/><rect x="24" y="36" width="5" height="5"/><rect x="32" y="36" width="5" height="5"/></g></svg></div>
<div class="stage-icon" style="left:963px"><svg viewBox="0 0 58 58" aria-hidden="true"><g fill="none" stroke="var(--navy)" stroke-width="1.8"><rect x="14" y="34" width="6" height="10"/><rect x="23" y="30" width="6" height="14"/><rect x="32" y="26" width="6" height="18"/><line x1="11" y1="44" x2="47" y2="44"/><polyline points="13,30 24,22 31,25 44,14"/><polyline points="38,14 44,14 44,20"/></g></svg></div>

<div class="stage-label" style="left:459px">Research</div>
<div class="stage-label" style="left:571px">Concept</div>
<div class="stage-label" style="left:674px">Design</div>
<div class="stage-label" style="left:778px">Prototype</div>
<div class="stage-label" style="left:885px">Pilot</div>
<div class="stage-label" style="left:995px">Market uptake</div>

<!-- Pillars -->
<section class="pillar elca">
  <h2>Environmental Life Cycle<br>Assessment (eLCA)</h2>
  <div class="pillar-art" role="img" aria-label="Globe with green leaves illustration" style="left:12px;top:74px;width:64px;height:72px;background:radial-gradient(circle,#7fa94a,#3f7a12)"></div>
  <ul>
    <li>Quantification of environmental impacts and benefits</li>
    <li>Comparison with a reference system</li>
    <li>Carbon footprint and broader impact categories</li>
    <li>ISO 14040/44, accredited models and databases</li>
  </ul>
</section>

<section class="pillar slca">
  <h2>Social Life Cycle Assessment<br>(S-LCA)</h2>
  <div class="pillar-art" role="img" aria-label="Group of people above a handshake illustration" style="left:9px;top:74px;width:62px;height:82px;background:radial-gradient(circle,#6db3b9,#16818a)"></div>
  <ul>
    <li>Assessment of social impacts across the life cycle</li>
    <li>Working conditions, health &amp; safety, human rights</li>
    <li>Stakeholder perspective and global value chains</li>
    <li>Social hotspot identification and relevant databases</li>
  </ul>
</section>

<section class="pillar lcc">
  <h2>Life Cycle Costing<br>(LCC)</h2>
  <svg class="abs" style="left:27px;top:74px" width="58" height="92" viewBox="0 0 58 92" aria-hidden="true">
    <circle cx="20" cy="19" r="17" fill="none" stroke="var(--orange)" stroke-width="3"/>
    <text x="20" y="27" text-anchor="middle" font-family="Source Sans 3, Arial, sans-serif" font-weight="700" font-size="22" fill="var(--orange)">€</text>
    <g fill="var(--orange)"><rect x="1" y="72" width="11" height="19"/><rect x="15" y="64" width="11" height="27"/><rect x="29" y="58" width="11" height="33"/><rect x="43" y="48" width="11" height="43"/></g>
    <polyline points="1,60 14,48 24,54 50,32" fill="none" stroke="var(--orange)" stroke-width="3"/>
    <path d="M44 30 L54 28 L52 38 Z" fill="var(--orange)"/>
  </svg>
  <ul>
    <li>Economic assessment across the life cycle</li>
    <li>Cost-benefit and techno-economic evaluation</li>
    <li>Infrastructure analyses and market screening</li>
    <li>Roll-out scenarios and cost drivers</li>
  </ul>
</section>

<!-- Balancing -->
<section class="box balance">
  <div class="pillar-art" role="img" aria-label="Circular arrows in green, teal and orange" style="left:12px;top:4px;width:52px;height:52px;background:conic-gradient(var(--teal) 0 33%,var(--orange) 33% 66%,var(--green) 66%);-webkit-mask:radial-gradient(circle,transparent 14px,#000 15px);mask:radial-gradient(circle,transparent 14px,#000 15px)"></div>
  <div class="balance-text">Balancing ecology, social<br>aspects and economy</div>
</section>

<!-- Benefits -->
<section class="box benefits">
  <svg class="abs" style="left:17px;top:12px" width="112" height="112" viewBox="0 0 112 112" aria-hidden="true">
    <circle cx="56" cy="56" r="53" fill="var(--white)" stroke="var(--navy)" stroke-width="3.5"/>
    <g fill="none" stroke="var(--navy)" stroke-width="2.2" stroke-linejoin="round">
      <rect x="30" y="26" width="46" height="62" rx="3"/>
      <rect x="46" y="20" width="16" height="9" rx="2"/>
      <polyline points="37,42 41,46 47,38"/><line x1="51" y1="43" x2="68" y2="43"/>
      <polyline points="37,58 41,62 47,54"/><line x1="51" y1="59" x2="66" y2="59"/>
      <polyline points="37,74 41,78 47,70"/><line x1="51" y1="75" x2="62" y2="75"/>
      <path d="M84 40 L70 70 L67 78 L73 72 L87 42 Z"/>
    </g>
  </svg>
  <h2>Integrated Process Assessment – Concrete Benefits</h2>
</section>

<div class="benefit" style="left:387px;top:736px"><svg viewBox="0 0 15 15" aria-hidden="true"><circle cx="7.5" cy="7.5" r="7.5" fill="var(--navy)"/><polyline points="4,7.6 6.5,10 11,5" fill="none" stroke="#fff" stroke-width="1.6"/></svg>Early identification of opportunities and risks</div>
<div class="benefit" style="left:387px;top:761px"><svg viewBox="0 0 15 15" aria-hidden="true"><circle cx="7.5" cy="7.5" r="7.5" fill="var(--navy)"/><polyline points="4,7.6 6.5,10 11,5" fill="none" stroke="#fff" stroke-width="1.6"/></svg>Sound decision support</div>
<div class="benefit" style="left:387px;top:785px"><svg viewBox="0 0 15 15" aria-hidden="true"><circle cx="7.5" cy="7.5" r="7.5" fill="var(--navy)"/><polyline points="4,7.6 6.5,10 11,5" fill="none" stroke="#fff" stroke-width="1.6"/></svg>Comparison of technologies and<br>product option</div>
<div class="benefit" style="left:679px;top:736px"><svg viewBox="0 0 15 15" aria-hidden="true"><circle cx="7.5" cy="7.5" r="7.5" fill="var(--navy)"/><polyline points="4,7.6 6.5,10 11,5" fill="none" stroke="#fff" stroke-width="1.6"/></svg>Iterative feedback for<br>development decisions</div>
<div class="benefit" style="left:679px;top:774px"><svg viewBox="0 0 15 15" aria-hidden="true"><circle cx="7.5" cy="7.5" r="7.5" fill="var(--navy)"/><polyline points="4,7.6 6.5,10 11,5" fill="none" stroke="#fff" stroke-width="1.6"/></svg>Holistic view of ecological, social<br>and economic performance</div>

<!-- Connectors, arrows, timeline, footer rules -->
<svg class="overlay" width="1200" height="926" viewBox="0 0 1200 926" aria-hidden="true">
  <path d="M387 222 L404 238.5 L387 255 Z" fill="var(--navy)"/>
  <line x1="461" y1="277" x2="992" y2="277" stroke="var(--navy)" stroke-width="2"/>
  <g fill="var(--navy)">
    <circle cx="461" cy="277" r="6"/><circle cx="569" cy="277" r="6"/><circle cx="671" cy="277" r="6"/>
    <circle cx="775" cy="277" r="6"/><circle cx="884" cy="277" r="6"/><circle cx="992" cy="277" r="6"/>
    <path d="M514 229 L523 238 L514 247 Z"/><path d="M618 229 L627 238 L618 247 Z"/>
    <path d="M722 229 L731 238 L722 247 Z"/><path d="M826 229 L835 238 L826 247 Z"/>
    <path d="M935 229 L944 238 L935 247 Z"/>
  </g>
  <polyline points="243,583 243,634 413,634" fill="none" stroke="var(--green)" stroke-width="2"/>
  <polyline points="904,583 904,634 720,634" fill="none" stroke="var(--orange)" stroke-width="2"/>
  <path d="M566 667 H576 V676 H583 L571 688 L559 676 H566 Z" fill="var(--navy)"/>
  <polyline points="1066,236 1103,236 1103,751 949,751" fill="none" stroke="var(--navy)" stroke-width="2.2" stroke-dasharray="7 6"/>
  <path d="M1052 236 L1067 226 L1067 246 Z" fill="var(--navy)"/>
  <path d="M933 751 L949 740 L949 762 Z" fill="var(--navy)"/>
  <line x1="83" y1="866" x2="310" y2="866" stroke="var(--navy)" stroke-width="1.8"/>
  <line x1="805" y1="866" x2="1050" y2="866" stroke="var(--navy)" stroke-width="1.8"/>
  <circle cx="341" cy="866" r="21" fill="#fff" stroke="var(--navy)" stroke-width="2.4"/>
  <g fill="none" stroke="var(--navy)" stroke-width="1.4">
    <circle cx="341" cy="866" r="12"/><ellipse cx="341" cy="866" rx="5.5" ry="12"/>
    <line x1="329" y1="866" x2="353" y2="866"/><line x1="331" y1="860" x2="351" y2="860"/><line x1="331" y1="872" x2="351" y2="872"/>
  </g>
</svg>

<p class="abs footer-text">Broadly applicable to diverse technologies, processes and products</p>
</body>
</html>
```